Zelvora - Creative Robotics

We are a software house for Audio Visual Systems integration/automation and home automation. we develop innovative software to automate a variety of devices mainly related to audio visuals and we design touch panel user interfaces to control these systems.

We would like to see designs that stick to our colours and theme, which you can find on our webpage www.zelvora-sample.com.au

The final design should communicate touch panels, innovation, software and automation.

Industry/Entity Type

Software

Requirements
Must have
• The business card must show the following information:
Name example : Derek Halvey
Qualification example: B Eng ICT(CompSys) Dip EngPrac
Title example : Control Systems Programmer
Mobile Phone, Company phone, Email address ,Company website

```html
<!DOCTYPE html>
<html lang="en">
<head>
<meta charset="UTF-8">
<title>Zelvora - Creative Robotics | Business Card</title>
<link rel="stylesheet" href="https://fonts.googleapis.com/css2?family=Nunito:wght@700;800&family=Questrial&display=swap">
<style>
  :root {
    --backdrop: #1c1c1e;
    --card-white: #ffffff;
    --brand-blue: #0f79c9;
    --brand-blue-light: #2a93dd;
    --brand-blue-deep: #0a62ae;
    --brand-green: #24a055;
    --ink: #4a4a4a;
    --ink-soft: #7a7a7a;
    --rule: #cfcfcf;
  }
  * { box-sizing: border-box; margin: 0; padding: 0; }
  html, body {
    width: 1200px; height: 675px; overflow: hidden;
    background: var(--backdrop);
  }
  .stage {
    position: relative; width: 1200px; height: 675px;
    display: flex; align-items: center; justify-content: center; gap: 40px;
  }
  .card {
    position: relative; width: 540px; height: 309px;
    overflow: hidden;
  }

  /* Front */
  .card--front { background: var(--card-white); font-family: "Questrial", sans-serif; color: var(--ink); }
  .brand {
    position: absolute; left: 36px; top: 96px;
    display: flex; align-items: center; gap: 12px;
  }
  .brand__square {
    width: 46px; height: 46px; border-radius: 7px;
    background: var(--brand-green);
  }
  .brand__text { display: flex; flex-direction: column; }
  .brand__name {
    font-family: "Nunito", sans-serif; font-weight: 800;
    font-size: 40px; line-height: 1; color: var(--brand-blue);
    letter-spacing: -0.5px;
  }
  .brand__tagline {
    align-self: flex-end; font-family: "Nunito", sans-serif; font-weight: 700;
    font-size: 8.5px; color: var(--ink); margin-top: 1px;
  }
  .divider {
    position: absolute; left: 36px; right: 30px; top: 176px;
    height: 1px; background: var(--rule);
  }
  .contact {
    position: absolute; right: 30px; top: 30px; width: 220px; text-align: right;
  }
  .contact__name {
    font-family: "Nunito", sans-serif; font-weight: 800;
    font-size: 17px; color: var(--brand-blue); line-height: 1.1;
  }
  .contact__title { font-size: 12.5px; color: var(--ink); margin-top: 2px; }
  .contact__rule { height: 1px; background: var(--rule); margin: 7px 0 8px; }
  .contact__list { list-style: none; font-size: 11.5px; line-height: 1.55; }
  .contact__list li { display: flex; justify-content: flex-end; align-items: center; gap: 6px; }
  .contact__list li.contact__email { margin-top: 8px; }
  .icon { width: 10px; height: 10px; fill: var(--brand-green); flex: none; }
  .address {
    position: absolute; left: 36px; bottom: 34px;
    font-size: 13px; line-height: 1.3; color: var(--ink);
  }
  .address__web {
    font-family: "Nunito", sans-serif; font-weight: 800;
    color: var(--brand-green); font-size: 12.5px; margin-top: 2px;
  }

  /* Back */
  .card--back {
    background: radial-gradient(ellipse at 50% 40%, var(--brand-blue-light) 0%, var(--brand-blue) 55%, var(--brand-blue-deep) 100%);
    color: var(--card-white);
  }
  .back-brand {
    position: absolute; left: 0; right: 0; top: 104px;
    display: flex; justify-content: center; align-items: center; gap: 14px;
  }
  .back-brand__square {
    width: 58px; height: 58px; border-radius: 9px; background: var(--card-white);
  }
  .back-brand__text { display: flex; flex-direction: column; }
  .back-brand__name {
    font-family: "Nunito", sans-serif; font-weight: 800;
    font-size: 50px; line-height: 1; letter-spacing: -0.5px;
  }
  .back-brand__tagline {
    align-self: flex-end; font-family: "Nunito", sans-serif; font-weight: 700; font-size: 10px;
  }
  .back-web {
    position: absolute; left: 0; right: 0; bottom: 52px; text-align: center;
    font-family: "Nunito", sans-serif; font-weight: 700; font-size: 11.5px;
  }
</style>
</head>
<body>
<main class="stage">
  <section class="card card--front" aria-label="Business card front">
    <div class="brand">
      <div class="brand__square"></div>
      <div class="brand__text">
        <span class="brand__name">zelvora</span>
        <span class="brand__tagline">Creative Robotics</span>
      </div>
    </div>

    <div class="contact">
      <p class="contact__name">Tomas Reyvik</p>
      <p class="contact__title">Principal</p>
      <div class="contact__rule"></div>
      <ul class="contact__list">
        <li>555.013.4827
          <svg class="icon" viewBox="0 0 10 10" aria-hidden="true"><path d="M1 3 Q5 0 9 3 L8 4.5 L6.5 3.8 L6.5 3 Q5 2.5 3.5 3 L3.5 3.8 L2 4.5 Z M2.5 5 H7.5 L8.5 9 H1.5 Z"/></svg>
        </li>
        <li>555.017.2290
          <svg class="icon" viewBox="0 0 10 10" aria-hidden="true"><rect x="2.5" y="0.5" width="5" height="9" rx="1"/></svg>
        </li>
        <li class="contact__email">tomas@zelvora-sample.com.au
          <svg class="icon" viewBox="0 0 10 10" aria-hidden="true"><path d="M0.5 2 H9.5 V8 H0.5 Z" /><path d="M0.5 2 L5 5.5 L9.5 2" fill="none" stroke="#fff" stroke-width="0.8"/></svg>
        </li>
      </ul>
    </div>

    <div class="divider"></div>

    <div class="address">
      <p>48 Harlow Lane</p>
      <p>Springfield, ZZ 00000</p>
      <p class="address__web">www.zelvora-sample.com.au</p>
    </div>
  </section>

  <section class="card card--back" aria-label="Business card back">
    <div class="back-brand">
      <div class="back-brand__square"></div>
      <div class="back-brand__text">
        <span class="back-brand__name">zelvora</span>
        <span class="back-brand__tagline">Creative Robotics</span>
      </div>
    </div>
    <p class="back-web">www.zelvora-sample.com.au</p>
  </section>
</main>
</body>
</html>
```